Letterhead design for Sleep Consulting Business

I'm looking for a new letterhead (heading/footer) design for my Sleep Consulting Business, I work with families to help their children improve their sleep.

The heading/footer will used in Microsoft Word Only-to be used for all of my documents such as writing Sleep Plans. I need to utilize as much working space in the document as possible. This will NOT be printed out on paper- it will only be used for heading/footer on microsoft word, then emailed to clients, who may print it at home.

My brand colors:
Dark Blue Hex: 1F2A42
Lighter Blueish Hex: 90BEC9
You're welcome to check out my website for inspiration- it is freshly created with other colors as well, and I love the outcome. www.hollowpinerest.com

Target Market(s)

Tired parents

Font styles to use
Script
Other font styles liked:
• Great Vibe, Lato or Just Another Hand are all used currently for my brand. Open to other options.

Requirements
Must have
• The letterhead (heading/footer) MUST be kept narrow (height-wise), so I have plenty of space on my document, while including important information.

It should look professional on screen, and when printed.

Must include my business name OR logo (Hollow Pine Sleep Consulting), and my email address. Mara@hollowpinerest.com

Website is optional, not required, just if you need to fill in a spot: www.hollowpinerest.com

```html
<!DOCTYPE html>
<html lang="en">
<head>
<meta charset="utf-8">
<title>Hollow Pine Sleep Consulting Letterhead</title>
<link href="https://fonts.googleapis.com/css2?family=Dancing+Script:wght@600&family=Lato:ital,wght@0,400;0,700;1,700&family=Quicksand:wght@400;500&display=swap" rel="stylesheet">
<style>
  :root {
    --navy: #1f2a42;
    --sky: #90bec9;
    --ink: #2a2a2a;
    --accent-red: #a50d0d;
    --muted: #666;
    --backdrop: #e4e4e4;
    --paper: #ffffff;
  }
  * { margin: 0; padding: 0; box-sizing: border-box; }
  html, body { width: 1082px; height: 1200px; overflow: hidden; background: var(--backdrop); }
  .letterhead {
    position: absolute; left: 104px; top: 0;
    width: 874px; height: 1200px;
    background: var(--paper); overflow: hidden;
    font-family: "Quicksand", sans-serif; color: var(--ink);
  }
  .brand { position: absolute; left: 43px; top: 56px; display: flex; align-items: center; gap: 14px; }
  .brand-dot { width: 64px; height: 64px; border-radius: 50%; background: var(--sky); flex: none; }
  .brand-name { font-family: "Lato", sans-serif; font-weight: 400; font-size: 27px; line-height: 1.2; color: var(--navy); }
  .header-title {
    position: absolute; right: 26px; top: 34px;
    font-family: "Dancing Script", cursive; font-weight: 600; font-size: 22px; color: var(--navy);
  }
  .contact {
    position: absolute; left: 629px; top: 73px; height: 67px;
    border-left: 1.5px solid #3b6fa6; padding-left: 11px;
    font-family: "Lato", sans-serif; font-size: 13px; color: #111; list-style: none;
  }
  .contact li { display: flex; align-items: center; gap: 5px; height: 22px; }
  .contact svg { width: 11px; height: 11px; flex: none; }
  .recipient { position: absolute; left: 87px; top: 219px; }
  .recipient .to { font-size: 16px; font-weight: 500; color: #000; margin-bottom: 17px; }
  .recipient .name { font-size: 17px; color: var(--accent-red); line-height: 1.05; letter-spacing: 0.4px; }
  .recipient .role { font-size: 11.5px; color: var(--muted); line-height: 1.1; }
  .recipient .line { font-size: 17.5px; font-weight: 500; line-height: 19.5px; letter-spacing: 0.4px; }
  .para {
    position: absolute; left: 87px; width: 740px;
    font-size: 15.6px; line-height: 19.6px; letter-spacing: 1.4px; white-space: nowrap;
  }
  .regards { position: absolute; left: 87px; top: 959px; font-family: "Lato", sans-serif; font-weight: 700; font-style: italic; font-size: 14px; color: #000; }
  .signature { position: absolute; left: 87px; top: 990px; width: 100px; height: 30px; background: #ececef; border-radius: 3px; }
  .corner-decoration {
    position: absolute; right: 0; bottom: 0; width: 640px; height: 280px;
    background: linear-gradient(160deg, rgba(31,42,66,0) 45%, rgba(31,42,66,0.55) 75%, var(--navy) 100%);
  }
</style>
</head>
<body>
<main class="letterhead">
  <div class="brand">
    <span class="brand-dot"></span>
    <span class="brand-name">Hollow Pine<br>Sleep Consulting</span>
  </div>

  <div class="header-title">Hollow Pine Sleep Consulting</div>
  <ul class="contact">
    <li><svg viewBox="0 0 24 24"><path fill="#1f2a42" d="M6.6 10.8a15 15 0 0 0 6.6 6.6l2.2-2.2c.3-.3.7-.4 1-.2 1.1.4 2.3.6 3.6.6.6 0 1 .4 1 1V20c0 .6-.4 1-1 1A17 17 0 0 1 3 4c0-.6.4-1 1-1h3.5c.6 0 1 .4 1 1 0 1.3.2 2.5.6 3.6.1.3 0 .7-.2 1z"/></svg>555-201-4837</li>
    <li><svg viewBox="0 0 24 24"><rect x="2" y="5" width="20" height="14" fill="none" stroke="#1f2a42" stroke-width="2"/><path d="M2 5l10 8 10-8" fill="none" stroke="#1f2a42" stroke-width="2"/></svg>Mara@hollowpinerest.com</li>
    <li><svg viewBox="0 0 24 24"><circle cx="12" cy="12" r="10" fill="#1f2a42"/><path d="M2 12h20M12 2c3 3 3 17 0 20M12 2c-3 3-3 17 0 20" fill="none" stroke="#fff" stroke-width="1.5"/></svg>&nbsp;www.hollowpinerest.com</li>
  </ul>

  <section class="recipient">
    <p class="to">TO</p>
    <p class="name">WHITAKER</p>
    <p class="role">Director</p>
    <p class="line">Design Studio</p>
    <p class="line">A: 145 565 254</p>
    <p class="line">B:8178&nbsp; 545 475</p>
  </section>

  <p class="para" style="top:370px">Lorem ipsum dolor sit amet, consectetur adipiscing elit. Vestibulum consectetur<br>egestas metus, quis scelerisque tortor consectetur sed. Nullam sit amet lorem sed<br>arcu faucibus semper. Vestibulum ante ipsum primis in faucibus orci luctus et<br>ultrices posuere cubilia Curae; Sed sagittis arcu ut ligula molestie malesuada.<br>Suspendisse posuere tincidunt elit, at ullamcorper augue blandit vitae.</p>
  <p class="para" style="top:487px">Cras egestas vestibulum pulvinar. Donec iaculis imperdiet hendrerit. Sed mollis,<br>enim quis hendrerit dictum, tortor mauris vulputate ligula, viverra porta magna<br>libero at mi. Integer odio nisl, luctus nec dui in, rutrum sollicitudin nisi. Suspendisse<br>nec erat eros.</p>
  <p class="para" style="top:585px">Sed dictum quam arcu, sit amet ullamcorper orci faucibus eget. Morbi finibus ante<br>at risus commodo, nec ullamcorper nulla tincidunt. Integer eu molestie nulla, sed<br>consequat tortor. Sed ullamcorper congue metus, vitae dictum nibh luctus sed.<br>Suspendisse ornare purus fermentum, viverra elit sed, bibendum ex. Vivamus<br>semper diam vel diam laoreet rutrum. Ut porta fermentum velit. Vestibulum vitae<br>semper nisl. Sed facilisis at ex et vestibulum. Donec at magna ut eros pulvinar<br>hendrerit.</p>
  <p class="para" style="top:761px">Sed dictum quam arcu, sit amet ullamcorper orci faucibus eget. Morbi finibus ante<br>at risus commodo, nec ullamcorper nulla tincidunt. Integer eu molestie nulla, sed<br>consequat tortor. Sed ullamcorper congue metus, vitae dictum nibh luctus sed.<br>Suspendisse ornare purus fermentum, viverra elit sed, bibendum ex.</p>
  <p class="para" style="top:860px">Vivamus semper diam vel diam laoreet rutrum. Ut porta fermentum velit.<br>Vestibulum vitae semper nisl. Sed facilisis at ex et vestibulum. Donec at magna ut<br>eros pulvinar hendrerit.</p>

  <p class="regards">Regards,</p>
  <div class="signature" role="img" aria-label="Handwritten signature"></div>

  <div class="corner-decoration" role="img" aria-label="Decorative navy corner accent"></div>
</main>
</body>
</html>
```